Commercial Rooftop Solar business needs a website

We need a website with fantastic appeal for a new company based in Melbourne called Brightvale Energy. We design and install solar energy systems for commercial applications across Australia. Our market is to focus on small to medium businesses looking for solar solutions, but we will also provide our service for residential customers. We would like a beautiful 'front page' feel to our home page, using photographs of solar PV systems and/or natural imagery. Our logo uses the colours orange and black, which could easily be echoed in photographic imagery of sunset and sunrise, for example. The design should communicate quiet confidence and professionalism to a corporate marketplace.

NEW POINTS FOR BRIEF: This design also needs to be flexible to allow for additional future content, including a Support page with sub pages, FAQ's, and a Blog.

As part of this design project, we will require the coding for the website to be completed by the designer.

We have seen some websites, which we like the look and feel of: these are listed below.

keenroofpower.com.au:

• Beautiful images underlaying brief text selling points.
• Simple ‘front cover’ style home page with elegant drop-down menu, stylish simple font style.
• Home page invites exploration through the menu links, rather than trying to provide all the information up front.
• Company logo and name in the top left hand corner, contact details accessible at top right hand, seems consistent in most sites.

tolvaenergy.com.au

brinkeltpower.com:
• Same element as the others is the front-page style home page with beautiful images underlying text.

We have a webpage that we started uploading content to. You can use some of the content there in your designs: www.brightvaleenergy.com.au

Technical Specifications:
PAGES:

Home

About Us

Solutions - Commercial
- Residential

Products - Solar Panels - Morvo Falcon, Morvo CELT, Morvo KT
- Solar Inverters - Valtrex, SunPivot
- Monitoring systems - Lumen Metrics
- Batteries - QD

- Datasheets have been provided for reference but if it's too much work, you can use generic text and we will provide content later.

Contact Us

FUTURE PAGES (Please consider in structure, where links could be placed):

Support

FAQ's

Blog.

We could provide some content for the Support page soon, but the Blog and FAQ's are future pages which we don't want highlighted in the design as we don't yet have content.

Phone: 1800 7 VOLTA
Email: sales@brightvaleenergy.com.au

Currently, I do not have images and text available. Please
use placeholders in the meantime. The final text and images will be uploaded for the winner once a winning design has been selected.

Target Market(s)

Primary focus is on small to medium sized business owners. Those owners will have a house which may be suitable for solar so we want to cater to residential deeper in the website.

Industry/Entity Type

Solar Energy

Coding

Coded - Design and coding required

Number of Pages Required

5+ page

Colors
f78f20
0255a3

Requirements
Must have
• Logo as per attachments.
Nice to have
• Logo can have alternate colours Eg. White on Orange or Black etc. provided colour correct logo is shown somewhere eg. footer or contact page.
• In the active site, I'd like to have:
• Very slowly zooming images - barely perceptible.
• Title text that rolls into place
• Subtle movements
• See https://paylarkfinance.com.au/ for example

```html
<!DOCTYPE html>
<html lang="en">
<head>
<meta charset="utf-8">
<title>Brightvale Energy — Solar Energy Systems</title>
<link href="https://fonts.googleapis.com/css2?family=Nunito+Sans:wght@400;600;700&family=Open+Sans:ital,wght@0,400;0,600;1,400&display=swap" rel="stylesheet">
<style>
:root{
  --orange:#f05a1a;
  --orange-deep:#e24e12;
  --ink:#222222;
  --charcoal:#333333;
  --footer:#2b2b2b;
  --footer-base:#1c1c1c;
  --grey-bg:#efefef;
  --text:#555555;
  --muted:#8a8a8a;
  --white:#ffffff;
}
*{margin:0;padding:0;box-sizing:border-box}
html,body{width:1200px;height:3644px;overflow:hidden}
body{font-family:"Nunito Sans",Arial,sans-serif;color:var(--ink);background:var(--white);position:relative}
section,header,footer{position:absolute;left:0;width:1200px}
.abs{position:absolute}
a{color:inherit;text-decoration:none}

/* header */
.site-header{top:0;height:107px;background:var(--white)}
.brand{left:122px;top:32px;display:flex;align-items:center;gap:12px;font-weight:700;font-size:26px;color:var(--orange);letter-spacing:.5px}
.brand-dot{width:36px;height:36px;border-radius:50%;background:var(--orange)}
.main-nav{left:420px;top:0;height:107px;display:flex}
.main-nav a{position:relative;display:block;padding:0 22px;line-height:107px;font-size:17px;color:var(--ink);letter-spacing:.5px}
.main-nav a.active::before{content:"";position:absolute;left:12px;right:12px;top:0;height:5px;background:var(--orange)}
.header-phone{left:912px;top:40px;display:flex;align-items:center;gap:8px;font-size:19px;font-weight:600}

/* hero */
.hero{top:107px;height:556px}
.hero-photo{left:0;top:0;width:1200px;height:556px;background:linear-gradient(180deg,#5b5a78 0%,#b06a5a 28%,#e6955a 42%,#c9886a 50%,#5d6f98 60%,#2c4d88 78%,#1f3a6e 100%)}
.hero-title{left:0;width:1200px;top:180px;text-align:center;color:var(--white);font-size:37px;font-weight:600;letter-spacing:1.2px;line-height:51px;text-transform:uppercase}
.btn-solid{background:var(--orange);color:var(--white);font-size:16px;text-align:center;text-transform:uppercase;letter-spacing:.5px}
.hero .btn-solid{left:525px;top:294px;width:158px;height:41px;line-height:41px}
.dots{display:flex;gap:12px}
.dots span{width:13px;height:13px;border-radius:50%;background:var(--white)}
.hero .dots{left:555px;top:526px}
.hero .dots span:first-child{background:transparent;border:2px solid var(--white)}

/* about */
.about{top:663px;height:428px;text-align:center}
.about-mark{left:582px;top:44px;width:36px;height:36px;border-radius:50%;background:var(--orange)}
.section-title{font-size:30px;font-weight:600;letter-spacing:.5px;text-transform:uppercase}
.about .section-title{left:0;width:1200px;top:98px}
.about-copy{left:206px;width:788px;font-family:"Open Sans",Arial,sans-serif;font-size:14px;line-height:22px;color:var(--muted)}
.about-copy.first{top:160px}
.about-copy.second{top:218px}
.btn-outline{border:2px solid var(--orange);color:var(--orange);font-size:15px;text-align:center;text-transform:uppercase;letter-spacing:.5px}
.about .btn-outline{left:520px;top:323px;width:160px;height:44px;line-height:40px}

/* solutions */
.solutions{top:1091px;height:507px;background:var(--grey-bg)}
.solutions .section-title{left:0;width:1200px;top:42px;text-align:center;font-size:28px;color:var(--charcoal)}
.solution-card{top:94px;width:479px;height:358px;text-align:center;color:var(--white)}
.solution-card.commercial{left:119px;background:var(--orange)}
.solution-card.residential{left:598px;background:#353535}
.notch{left:586px;top:94px;width:0;height:0;border-left:12px solid transparent;border-right:12px solid transparent;border-top:14px solid var(--grey-bg)}
.solution-icon{position:absolute;left:179px;top:40px}
.solution-card h3{position:absolute;left:0;width:100%;top:188px;font-size:21px;font-weight:600;letter-spacing:.5px}
.solution-card p{position:absolute;left:45px;width:389px;top:222px;font-family:"Open Sans",Arial,sans-serif;font-size:12.5px;line-height:22px;opacity:.8}
.solution-card .btn-ghost{position:absolute;left:189px;top:285px;width:125px;height:38px;line-height:36px;border:1px solid var(--white);font-size:12px;letter-spacing:.5px}

/* why */
.why{top:1598px;height:476px}
.why-photo{left:0;top:0;width:1200px;height:476px;background:linear-gradient(180deg,#4b4862 0%,#8d6a6a 25%,#e29a55 42%,#9a7a70 52%,#3c4f78 64%,#23375d 100%)}
.why .section-title{left:121px;top:100px;color:var(--white);font-size:30px}
.why-copy{left:121px;width:445px;font-family:"Open Sans",Arial,sans-serif;font-size:14px;line-height:22px;color:#f3f3f3}
.why-copy.first{top:148px}
.why-copy.second{top:203px}
.why .btn-outline{left:121px;top:304px;width:146px;height:44px;line-height:40px;border-color:var(--white);color:var(--white)}

/* testimonials */
.testimonials{top:2074px;height:387px;background:var(--grey-bg)}
.testimonials .section-title{left:0;width:1200px;top:70px;text-align:center;color:var(--orange);font-size:28px}
.avatar{left:248px;top:120px;width:170px;height:170px;border-radius:50%;background:linear-gradient(160deg,#6d86a6,#c9b9aa 60%,#3a4a60);border:5px solid #34507a}
.quote-badge{left:378px;top:140px;width:38px;height:38px;border-radius:50%;background:var(--orange)}
.testimonial-text{left:440px;width:540px;top:140px;font-family:"Open Sans",Arial,sans-serif;font-style:italic;font-size:16px;line-height:29px;color:var(--muted)}
.testimonial-author{left:440px;top:250px;font-size:17px;font-weight:600;color:var(--ink)}
.testimonials .dots{left:547px;top:326px}
.testimonials .dots span{background:#bdbdbd}
.testimonials .dots span:first-child{background:transparent;border:2px solid #bdbdbd}

/* projects */
.projects{top:2461px;height:442px}
.projects .section-title{left:131px;top:35px;color:var(--orange);font-size:28px}
.project{top:87px;width:292px;text-align:center}
.project-photo{width:292px;height:172px}
.project h4{margin-top:30px;font-size:18px;font-weight:600;color:var(--ink)}
.project p{margin-top:10px;font-family:"Open Sans",Arial,sans-serif;font-size:12px;line-height:20px;color:var(--text)}
.project a{display:block;margin-top:6px;font-size:13px;color:var(--orange);text-transform:uppercase}

/* contact */
.contact{top:2903px;height:369px;background:linear-gradient(180deg,#f27a1e 0%,#f0691a 45%,#e2591a 100%)}
.contact-notch{left:576px;top:0;width:0;height:0;border-left:24px solid transparent;border-right:24px solid transparent;border-top:26px solid var(--white)}
.contact .section-title{left:0;width:1200px;top:55px;text-align:center;color:var(--white);font-size:26px;font-weight:400}
.field{background:var(--white);font-family:"Open Sans",Arial,sans-serif;font-size:13px;color:#777;padding:12px 14px}
.submit{left:515px;top:267px;width:155px;height:46px;line-height:46px;background:#111;color:var(--white);text-align:center;font-size:17px;font-weight:600;letter-spacing:.5px}

/* footer */
.site-footer{top:3272px;height:372px;background:var(--footer);color:#d5d5d5}
.footer-col h5{font-size:22px;font-weight:400;color:var(--white);margin-bottom:16px}
.footer-col li{list-style:none;font-size:14px;line-height:29px}
.contact-line{display:flex;align-items:center;gap:12px}
.social{display:flex;gap:8px}
.social span{width:38px;height:38px;border-radius:50%;border:2px solid #e0e0e0}
.footer-base{left:0;top:301px;width:1200px;height:71px;background:var(--footer-base);color:#9a9a9a;font-size:13px;text-align:center;line-height:71px}
</style>
</head>
<body>

<header class="site-header">
  <a class="brand abs" href="#"><span class="brand-dot"></span>Brightvale Energy</a>
  <nav class="main-nav abs">
    <a class="active" href="#">HOME</a>
    <a href="#">ABOUT US</a>
    <a href="#">SOLUTIONS</a>
    <a href="#">CONTACT US</a>
  </nav>
  <div class="header-phone abs">
    <svg width="20" height="20" viewBox="0 0 24 24" fill="none" stroke="#f05a1a" stroke-width="2"><path d="M5 3h4l2 5-2.5 1.5a11 11 0 0 0 6 6L16 13l5 2v4a2 2 0 0 1-2 2A17 17 0 0 1 3 5a2 2 0 0 1 2-2z"/></svg>
    (666) 555 0148
  </div>
</header>

<section class="hero">
  <div class="hero-photo abs" role="img" aria-label="Rows of solar panels under a sunset sky with hills"></div>
  <h1 class="hero-title abs">Design and install solar energy<br>systems for commercial</h1>
  <a class="btn-solid abs" href="#">Read more</a>
  <div class="dots abs"><span></span><span></span><span></span><span></span></div>
</section>

<section class="about">
  <div class="about-mark abs"></div>
  <h2 class="section-title abs">About Brightvale Energy</h2>
  <p class="about-copy first abs">commodo a mi Morbi ornare gravida elit Integer congue augue et malesuada iaculis ipsum dui aliquet felis at cursus magna nisl nec elit Praesent elementum elit at tellus nec ultricies sit</p>
  <p class="about-copy second abs">Amet porttitor mattis enim In massa libero interdum nec interdum vel blandit sed nulla In ullamcorper est eget tempor cursus neque mi consectetuer mi a ultricies massa est sed nisl Class aptent taciti sociosqu ad litora torquent per conubia nostra per inceptos hymenaeos Proin nulla arcu nonummy</p>
  <a class="btn-outline abs" href="#">Read more</a>
</section>

<section class="solutions">
  <h2 class="section-title abs">Our Solution</h2>
  <div class="solution-card commercial abs">
    <svg class="solution-icon" width="120" height="120" viewBox="0 0 120 120" fill="none" stroke="#fff" stroke-width="5">
      <circle cx="60" cy="60" r="50"/>
      <g fill="#fff" stroke="none"><rect x="44" y="38" width="20" height="46"/><rect x="66" y="52" width="14" height="32"/></g>
      <g fill="#f05a1a" stroke="none"><rect x="49" y="44" width="4" height="5"/><rect x="56" y="44" width="4" height="5"/><rect x="49" y="54" width="4" height="5"/><rect x="56" y="54" width="4" height="5"/><rect x="49" y="64" width="4" height="5"/><rect x="56" y="64" width="4" height="5"/></g>
    </svg>
    <h3>COMMERCIAL</h3>
    <p>Class aptent taciti sociosqu ad litora torquent per conubia nostra per inceptos hymenaeos Proin nulla</p>
    <a class="btn-ghost" href="#">READ MORE</a>
  </div>
  <div class="solution-card residential abs">
    <svg class="solution-icon" width="120" height="120" viewBox="0 0 120 120" fill="none" stroke="#fff" stroke-width="5">
      <circle cx="60" cy="60" r="50"/>
      <path d="M36 60 60 38l24 22M43 55v27h34V55" stroke-linejoin="round"/>
      <rect x="54" y="66" width="12" height="16" fill="#fff" stroke="none"/>
    </svg>
    <h3>RESIDENTIAL</h3>
    <p>Class aptent taciti sociosqu ad litora torquent per conubia nostra per inceptos hymenaeos Proin nulla</p>
    <a class="btn-ghost" href="#">READ MORE</a>
  </div>
  <div class="notch abs"></div>
</section>

<section class="why">
  <div class="why-photo abs" role="img" aria-label="Solar panel field at sunset with the sun low over distant hills"></div>
  <h2 class="section-title abs">Why We Are</h2>
  <p class="why-copy first abs">Praesent elementum elit at tellus nec ultricies sit amet porttitor mattis enim In massa libero interdum nec interdum</p>
  <p class="why-copy second abs">eget tempor cursus neque mi consectetuer mi a ultricies massa est sed nisl Class aptent taciti sociosqu ad litora torquent per conubia nostra per inceptos hymenaeos Proin nulla arcu nonummy luctus dictum eget fermentum et lorem</p>
  <a class="btn-outline abs" href="#">Read more</a>
</section>

<section class="testimonials">
  <h2 class="section-title abs">Testimonials</h2>
  <div class="avatar abs" role="img" aria-label="Portrait photo of the client giving the testimonial"></div>
  <div class="quote-badge abs">
    <svg width="38" height="38" viewBox="0 0 38 38" fill="#fff"><path d="M11 22c0-5 2-8 6-9v3c-2 1-3 2-3 3h3v6h-6zM20 22c0-5 2-8 6-9v3c-2 1-3 2-3 3h3v6h-6z"/></svg>
  </div>
  <p class="testimonial-text abs">Praesent elementum elit at tellus nec ultricies sit amet porttitor mattis enim In massa libero interdum nec interdum vel blandit sed nulla In ullamcorper est eget tempor cursus neque</p>
  <p class="testimonial-author abs">By Author Name</p>
  <div class="dots abs"><span></span><span></span><span></span><span></span></div>
</section>

<section class="projects">
  <h2 class="section-title abs">Recent Projects</h2>
  <article class="project abs" style="left:126px">
    <div class="project-photo" role="img" aria-label="Solar water heater on a red tiled roof" style="background:linear-gradient(180deg,#8ec4ec 0%,#cfd9e2 35%,#d8622e 55%,#b84a22 100%)"></div>
    <h4>Aonubia nostra inceptos</h4>
    <p>hymenaeos Proin nulla arcu nonummy luctus<br>dictum eget fermentum et lorem</p>
    <a href="#">Read more</a>
  </article>
  <article class="project abs" style="left:447px">
    <div class="project-photo" role="img" aria-label="Solar panels in front of a city skyline" style="background:linear-gradient(180deg,#9fc3e6 0%,#b9c8d6 45%,#5b7aa3 65%,#2f4f80 100%)"></div>
    <h4>Mauris vel lacus vitae</h4>
    <p>hymenaeos Proin nulla arcu nonummy luctus<br>dictum eget fermentum et lorem</p>
    <a href="#">Read more</a>
  </article>
  <article class="project abs" style="left:768px">
    <div class="project-photo" role="img" aria-label="Solar panels installed on a tiled roof under blue sky" style="background:linear-gradient(180deg,#5fa8e6 0%,#9ccbef 35%,#3c77b8 60%,#c9542a 100%)"></div>
    <h4>Donec convallis ped</h4>
    <p>hymenaeos Proin nulla arcu nonummy luctus<br>dictum eget fermentum et lorem</p>
    <a href="#">Read more</a>
  </article>
</section>

<section class="contact" role="img" aria-label="Orange toned photo of solar panels behind the contact form">
  <div class="contact-notch abs"></div>
  <h2 class="section-title abs">Contact Us</h2>
  <div class="field abs" style="left:172px;top:119px;width:277px;height:44px">Name</div>
  <div class="field abs" style="left:464px;top:119px;width:267px;height:44px">Email address</div>
  <div class="field abs" style="left:743px;top:119px;width:272px;height:44px">Phone</div>
  <div class="field abs" style="left:172px;top:172px;width:843px;height:75px">Message</div>
  <div class="submit abs">SUBMIT</div>
</section>

<footer class="site-footer">
  <div class="footer-col abs" style="left:131px;top:72px">
    <h5>Company</h5>
    <ul><li>About Us</li><li>Contact Us</li><li>Privacy Policy</li><li>Terms &amp; Condition</li></ul>
  </div>
  <div class="footer-col abs" style="left:350px;top:72px">
    <h5>Resources</h5>
    <ul><li>Solutions</li><li>Services</li><li>Projects</li></ul>
  </div>
  <div class="footer-col abs" style="left:547px;top:72px">
    <h5>Contact Us</h5>
    <ul>
      <li class="contact-line"><svg width="14" height="16" viewBox="0 0 14 18" fill="#ddd"><path d="M7 0a7 7 0 0 0-7 7c0 5 7 11 7 11s7-6 7-11a7 7 0 0 0-7-7zm0 10a3 3 0 1 1 0-6 3 3 0 0 1 0 6z"/></svg>27 Linden Row Suite 4 Melbourne VIC 3000</li>
      <li class="contact-line"><svg width="14" height="14" viewBox="0 0 24 24" fill="none" stroke="#ddd" stroke-width="2.5"><path d="M5 3h4l2 5-2.5 1.5a11 11 0 0 0 6 6L16 13l5 2v4a2 2 0 0 1-2 2A17 17 0 0 1 3 5a2 2 0 0 1 2-2z"/></svg>555.014.7731</li>
      <li class="contact-line"><svg width="15" height="12" viewBox="0 0 20 14" fill="none" stroke="#ddd" stroke-width="1.8"><rect x="1" y="1" width="18" height="12"/><path d="M1 1l9 7 9-7"/></svg>info@brightvaleenergy.com.au</li>
    </ul>
  </div>
  <div class="footer-col abs" style="left:887px;top:72px">
    <h5>Stay in Touch</h5>
    <div class="social"><span></span><span></span><span></span><span></span></div>
  </div>
  <div class="footer-base abs">© 2016 Company Name&nbsp; All right reserved</div>
</footer>

</body>
</html>
```